Packing for Razor Blade VELKORN

Dears: We need a packing design. The product is an Disposable Razor Blade. We are a company in Brazil.

The packing consists in a bag package which the Disposables Razos are placed. 5 units into each bag.

The bag is not 100% printed and should let a space to the customer see the razors inside. Some competitors uses oval circle. I attached competitor package (Dov Harborline)

The background color should be blue, this color tonality should vary its magnitude from dark blue to soft blue. Blue is a good color for personal care products because customer can take the impression of cleanness, especially for razor blade which has the fuction to shave.

You can feel free to add other colors however it can not be much colorfull because it may get trouble to printer company print it. Silver is good.

You can feel free to do details. You can feel free also to place the logo above the package or at bottom of it.

Dimmensions:
Heigh 24cm
Width 10cm

Featuring
- Featuring: Handle with Grip. In Portuguese - (Cabo Aderente)
- Featuring: 2 Razors. In portuguese - (Duas Lâminas)

Reason: I stayed many days with out providing feedbacks. I want to give more time for you .

Target Market(s)

Mans ( for woman we will design other package )

Requirements
Nice to have
• maybe some tears as a wet surface...
pls can feel free

```html
<!DOCTYPE html>
<html lang="en">
<head>
<meta charset="utf-8">
<title>VELKORN Disposable Razor Pack</title>
<link rel="stylesheet" href="https://fonts.googleapis.com/css2?family=Archivo:ital,wght@0,800;1,800;1,900&display=swap">
<style>
  :root {
    --navy: #0a174f;
    --royal: #0f2fa8;
    --bright: #1b55e6;
    --sky: #3d8fe0;
    --ice: #8fd0ff;
    --silver-light: #f2f4f6;
    --silver-mid: #b9bec4;
    --silver-dark: #7d848c;
    --white: #ffffff;
    --ink: #1c2230;
  }
  html, body {
    margin: 0;
    padding: 0;
    width: 1200px;
    height: 2880px;
    overflow: hidden;
    background: var(--navy);
  }
  .pack {
    display: block;
    width: 1200px;
    height: 2880px;
  }
  .brand-name {
    font-family: "Archivo", Arial, sans-serif;
    font-weight: 800;
    font-style: normal;
    fill: var(--white);
    letter-spacing: 2px;
  }
  .feature-text {
    font-family: "Archivo", Arial, sans-serif;
    font-weight: 800;
    font-style: italic;
    fill: var(--white);
    letter-spacing: 0.8px;
    paint-order: stroke;
    stroke: var(--ink);
    stroke-width: 1.6px;
  }
  .count-number {
    font-family: "Archivo", Arial, sans-serif;
    font-weight: 900;
    font-style: italic;
    fill: url(#silverText);
    stroke: var(--ink);
    stroke-width: 1px;
  }
  .count-label {
    font-family: "Archivo", Arial, sans-serif;
    font-weight: 900;
    font-style: italic;
    fill: var(--white);
    paint-order: stroke;
    stroke: var(--ink);
    stroke-width: 1.6px;
  }
</style>
</head>
<body>
<svg class="pack" viewBox="0 0 500 1200" preserveAspectRatio="none" xmlns="http://www.w3.org/2000/svg">
  <defs>
    <linearGradient id="bgBlue" x1="0" y1="0" x2="0.3" y2="1">
      <stop offset="0" stop-color="var(--navy)"/>
      <stop offset="0.45" stop-color="var(--royal)"/>
      <stop offset="0.75" stop-color="var(--bright)"/>
      <stop offset="1" stop-color="var(--sky)"/>
    </linearGradient>
    <radialGradient id="logoGlow" cx="0.5" cy="0.5" r="0.5">
      <stop offset="0.7" stop-color="#4aa8ff" stop-opacity="0.6"/>
      <stop offset="1" stop-color="#4aa8ff" stop-opacity="0"/>
    </radialGradient>
    <linearGradient id="windowFill" x1="0" y1="0" x2="1" y2="1">
      <stop offset="0" stop-color="var(--white)"/>
      <stop offset="1" stop-color="#f3f5f8"/>
    </linearGradient>
    <linearGradient id="silverTab" x1="0" y1="0" x2="1" y2="0">
      <stop offset="0" stop-color="var(--silver-dark)"/>
      <stop offset="0.35" stop-color="var(--silver-light)"/>
      <stop offset="0.7" stop-color="var(--silver-mid)"/>
      <stop offset="1" stop-color="var(--silver-dark)"/>
    </linearGradient>
    <linearGradient id="silverText" x1="0" y1="0" x2="0" y2="1">
      <stop offset="0" stop-color="var(--silver-light)"/>
      <stop offset="0.5" stop-color="var(--silver-mid)"/>
      <stop offset="1" stop-color="var(--silver-dark)"/>
    </linearGradient>
    <linearGradient id="productShot" x1="0" y1="0" x2="1" y2="1">
      <stop offset="0" stop-color="#a9dcf5"/>
      <stop offset="0.5" stop-color="#8e969f"/>
      <stop offset="1" stop-color="#4a5058"/>
    </linearGradient>
  </defs>

  <rect class="backdrop" width="500" height="1200" fill="url(#bgBlue)"/>

  <g class="sweep-stripes" fill="none" stroke-linecap="round">
    <path d="M-10 330 C130 230 310 170 510 150" stroke="#2a5fd0" stroke-width="8"/>
    <path d="M-10 352 C130 252 310 192 510 172" stroke="var(--sky)" stroke-width="6"/>
    <path d="M-10 372 C130 272 310 212 510 192" stroke="#6ab4f5" stroke-width="5"/>
    <path d="M-10 392 C130 292 310 232 510 212" stroke="var(--ice)" stroke-width="5"/>
    <path d="M-10 412 C130 312 310 252 510 232" stroke="#bfe6ff" stroke-width="4"/>
  </g>

  <path class="window-edge" d="M-5 438 C140 326 300 262 500 222 L500 236 L262 792 L-5 915 Z" fill="var(--silver-mid)"/>
  <path class="window" d="M-5 448 C140 336 300 272 480 236 L248 780 L-5 900 Z" fill="url(#windowFill)"/>

  <g class="diagonal-stripes" stroke-linecap="butt">
    <line x1="510" y1="250" x2="285" y2="800" stroke="#5aa6f0" stroke-width="6"/>
    <line x1="510" y1="290" x2="305" y2="810" stroke="var(--ice)" stroke-width="4"/>
    <line x1="510" y1="330" x2="325" y2="820" stroke="#5aa6f0" stroke-width="4"/>
    <line x1="510" y1="370" x2="345" y2="830" stroke="#bfe6ff" stroke-width="3"/>
  </g>

  <g class="logo">
    <ellipse cx="250" cy="100" rx="192" ry="60" fill="url(#logoGlow)"/>
    <ellipse cx="250" cy="100" rx="182" ry="52" fill="var(--navy)"/>
    <text class="brand-name" x="250" y="115" text-anchor="middle" font-size="44">VELKORN</text>
  </g>

  <rect class="product-shot" role="img" aria-label="Photo of a two-blade disposable razor with a silver grip handle, splashed with water"
        x="0" y="720" width="350" height="290" rx="16" fill="url(#productShot)"/>

  <g class="feature-tab">
    <polygon points="208,982 500,982 500,1052 180,1052" fill="url(#silverTab)"/>
    <text class="feature-text" x="478" y="1012" text-anchor="end" font-size="19">Handle With Grip</text>
    <text class="feature-text" x="478" y="1040" text-anchor="end" font-size="19">Cabo Aderente</text>
  </g>
  <g class="feature-tab">
    <polygon points="222,1070 500,1070 500,1142 196,1142" fill="url(#silverTab)"/>
    <text class="feature-text" x="478" y="1100" text-anchor="end" font-size="19">2 Razors</text>
    <text class="feature-text" x="478" y="1128" text-anchor="end" font-size="19">Duas Laminas</text>
  </g>

  <g class="pack-count">
    <text class="count-number" x="46" y="1172" font-size="62">5</text>
    <text class="count-label" x="98" y="1168" font-size="24">Pieces</text>
  </g>
</svg>
</body>
</html>
```